Anzeige zur Kundenakquise
Zielgruppe
Wir sind der größte unabhängige Versicherungsmakler Deutschlands.
https://www.vendler-tarifkreis.de/
Aufgabenstellung
Die Anzeige dient zur Kundenakquise. Der Flyer soll in erster Linie auf Trivolo veröffentlicht werden.
Sie soll Kunden anregen eine Nachricht an uns zu schicken und einen Termin bis zum 30.11.2018 zu vereinbaren um ihre KFZ-Versicherungen vergleichen zu lassen.
Der alte Flyer wird mit hochgeladen. Bitte den Text nicht 1 zu 1 übernehmen.
Farbe und Stil sollten übernommen werden.
Die Maße für Trivolo:
Empfohlene Bildgröße:
1.200 x 628 Pixel
Bildseitenverhältnis: 1,91:1
Auf Grund der Zusendung von mehrerern Flyer der Designer bitte ich die Anzahl auf 3 zu einigen, d.h. bitte senden Sie für eine Trivolo Slidekampane 3 Flyer als ein Projekt zu. Vielen Dank für Ihre Mühe.

```html
<!DOCTYPE html>
<html lang="de">
<head>
<meta charset="utf-8">
<title>Vendler Tarifkreis – KFZ-Versicherung bis zum 30.11</title>
<link rel="stylesheet" href="https://fonts.googleapis.com/css2?family=Roboto:wght@700;900&display=swap">
<style>
  :root {
    --green: #7ab51d;
    --green-light: #8cc63f;
    --ink: #4a4a4a;
    --white: #ffffff;
    --date-box: rgba(70, 70, 70, 0.78);
  }
  * { margin: 0; padding: 0; box-sizing: border-box; }
  html, body {
    width: 1200px;
    height: 628px;
    overflow: hidden;
    background: var(--white);
    font-family: "Roboto", Arial, sans-serif;
  }
  .ad {
    position: relative;
    width: 1200px;
    height: 628px;
    overflow: hidden;
    background: var(--white);
  }
  .hero-photo {
    position: absolute;
    left: 0; top: 0;
    width: 1200px; height: 500px;
    background:
      radial-gradient(ellipse 260px 200px at 840px 230px, rgba(225,170,120,0.55), transparent 70%),
      radial-gradient(ellipse 220px 140px at 790px 440px, rgba(240,200,40,0.85), transparent 75%),
      linear-gradient(100deg, #d9dde0 0%, #9fa3a6 22%, #5e6164 45%, #c9b89a 70%, #6d6f70 100%);
  }
  .date-box {
    position: absolute;
    left: 62px; top: 133px;
    width: 586px; height: 99px;
    background: var(--date-box);
    display: flex;
    align-items: center;
    padding-left: 26px;
    font-weight: 900;
    font-size: 80px;
    line-height: 1;
    color: var(--white);
    letter-spacing: 0.5px;
  }
  .date-box .date { color: var(--green-light); margin-left: 22px; }
  .headline-band {
    position: absolute;
    left: 0; top: 253px;
    width: 662px; height: 149px;
    background: var(--green);
    padding: 22px 0 0 88px;
    color: var(--white);
    font-weight: 700;
    font-size: 45px;
    line-height: 56px;
    letter-spacing: 0.3px;
  }
  .savings-badge {
    position: absolute;
    left: 878px; top: 273px;
    width: 226px; height: 226px;
    border-radius: 50%;
    background: var(--white);
    padding: 10px;
  }
  .savings-badge .disc {
    width: 100%; height: 100%;
    border-radius: 50%;
    background: var(--green);
    color: var(--white);
    display: flex;
    flex-direction: column;
    align-items: center;
    justify-content: center;
    transform: rotate(-14deg);
    font-weight: 700;
    text-align: center;
  }
  .savings-badge .small { font-size: 26px; line-height: 28px; }
  .savings-badge .big { font-size: 84px; line-height: 78px; font-weight: 900; }
  .cta {
    position: absolute;
    left: 0; top: 500px;
    width: 1200px; height: 128px;
    display: flex;
    align-items: center;
    justify-content: center;
    padding-right: 4px;
    font-weight: 700;
    font-size: 38px;
    color: var(--ink);
    letter-spacing: 0.2px;
  }
  .cta .accent { color: var(--green); margin: 0 11px; }
  .brand {
    position: absolute;
    left: 1086px; top: 533px;
    display: flex;
    align-items: center;
    gap: 6px;
    color: var(--ink);
    font-weight: 700;
    font-size: 14px;
    line-height: 16px;
  }
  .brand .mark {
    width: 14px; height: 14px;
    background: var(--green);
    flex: none;
  }
</style>
</head>
<body>
  <main class="ad">
    <div class="hero-photo" role="img" aria-label="Foto: junge Frau im gelben Hemd fährt ein silbernes Cabrio bei Sonnenschein"></div>

    <div class="date-box">BIS ZUM <span class="date">30.11</span></div>

    <h1 class="headline-band">SCHLUSS MIT TEUREN<br>KFZ-VERSICHERUNGEN</h1>

    <div class="savings-badge">
      <div class="disc">
        <span class="small">BIS ZU</span>
        <span class="big">40%</span>
        <span class="small">SPAREN!</span>
      </div>
    </div>

    <p class="cta">VEREINBAREN SIE <span class="accent">GLEICH</span> EINEN TERMIN!</p>

    <div class="brand">
      <span class="mark"></span>
      <span class="brand-name">VENDLER<br>TARIFKREIS</span>
    </div>
  </main>
</body>
</html>
```